New business card design needed for Diesel Fitting (Mechanical) Company

We need a new business card for our company called "Gumtree Engine Works" that showcases our logo and business details.
Target Market(s)
Owners of all makes and models of vehicles, trucks, plant and machinery.
Industry/Entity Type
Mechanical
Contact Information for Business Card
The business card details need to include the following: Owners/Directors: Doug & Marisol Brent-Coyle ABN: 41 917 302 846 Address: 317 Wattlebrook Street DALBEEN CREEK QLD 4791 Postal Address: PO Box 5791 DALBEEN CREEK QLD 4791 Website: www.gewservice.com.au Phone: 4712 9083 Mobile: 0438 175 906 Emails: sales@gewservice.com.au; admin@gewservice.com.au; accounts@gewservice.com.au; parts@gewservice.com.au; office@gewservice.com.au, reception@gewservice.com.au
Look and feel

```html
<!DOCTYPE html>
<html lang="en">
<head>
<meta charset="utf-8">
<title>Gumtree Engine Works – Business Card</title>
<link rel="stylesheet" href="https://fonts.googleapis.com/css2?family=Roboto+Condensed:wght@400;700&family=Roboto:wght@400&display=swap">
<style>
  :root {
    --page-bg: #e4e4e4;
    --orange-light: #f58a3c;
    --orange-dark: #ec5a1c;
    --panel-dark: #1c1c1c;
    --panel-mid: #2c2c2c;
    --text-light: #ffffff;
  }
  * { margin: 0; padding: 0; box-sizing: border-box; }
  html, body { width: 1200px; height: 1200px; overflow: hidden; }
  body {
    background: var(--page-bg);
    font-family: "Roboto", Arial, sans-serif;
    position: relative;
  }
  .card {
    position: absolute;
    left: 257px;
    width: 686px;
    height: 392px;
    border-radius: 22px;
    overflow: hidden;
  }
  .card--front {
    top: 165px;
    background: linear-gradient(160deg, var(--orange-light), var(--orange-dark));
  }
  .card--back {
    top: 653px;
    background: radial-gradient(ellipse at 50% 45%, var(--panel-mid), var(--panel-dark) 75%);
  }
  .front-panel { position: absolute; inset: 0; }
  .details {
    position: absolute;
    left: 38px;
    top: 82px;
    color: var(--text-light);
    font-size: 15.5px;
    line-height: 19px;
  }
  .details .name {
    font-family: "Roboto Condensed", Arial Narrow, sans-serif;
    font-weight: 700;
    font-size: 23px;
    line-height: 26px;
  }
  .details .role { margin-top: 1px; }
  .details .group { margin-top: 8px; }
  .contact-line { display: flex; align-items: center; gap: 7px; }
  .contact-line svg { width: 12px; height: 12px; flex: none; }
  .brand-name {
    position: absolute;
    font-family: "Roboto Condensed", Arial Narrow, sans-serif;
    font-weight: 700;
    color: var(--text-light);
    text-align: center;
    line-height: 1.05;
  }
  .card--front .brand-name {
    left: 380px; width: 290px; top: 160px;
    font-size: 32px;
  }
  .card--back .brand-name {
    left: 0; width: 100%; top: 130px;
    font-size: 48px;
  }
  .emails {
    position: absolute;
    left: 0; width: 100%;
    top: 315px;
    text-align: center;
    color: var(--text-light);
    font-family: "Roboto Condensed", Arial Narrow, sans-serif;
    font-size: 16px;
    line-height: 20px;
  }
</style>
</head>
<body>
  <section class="card card--front">
    <svg class="front-panel" viewBox="0 0 686 392" aria-hidden="true">
      <defs>
        <radialGradient id="darkPanel" cx="0.75" cy="0.5" r="0.7">
          <stop offset="0" stop-color="#2e2e2e"/>
          <stop offset="1" stop-color="#151515"/>
        </radialGradient>
      </defs>
      <path d="M345 0 C285 130 285 265 312 392 L686 392 L686 0 Z" fill="url(#darkPanel)"/>
    </svg>

    <div class="details">
      <div class="name">Doug &amp; Marisol Brent-Coyle</div>
      <div class="role">Owners/Directors</div>
      <div>ABN: 41 917 302 846</div>
      <div class="group">317 Wattlebrook Street<br>Dalbeen Creek Qld 4791</div>
      <div class="group">PO Box 5791<br>Dalbeen Creek Qld 4791</div>
      <div class="group">
        <div class="contact-line">
          <svg viewBox="0 0 12 12"><path d="M2.5 1 L4.5 1 L5 3.5 L3.8 4.5 C4.5 6 5.8 7.3 7.4 8 L8.5 6.9 L11 7.5 L11 9.5 C11 10.3 10.3 11 9.5 11 C5 11 1 7 1 2.5 C1 1.7 1.7 1 2.5 1 Z" fill="#fff"/></svg>
          <span>4712 9083</span>
        </div>
        <div class="contact-line">
          <svg viewBox="0 0 12 12"><rect x="3" y="0.8" width="6" height="10.4" rx="1" fill="none" stroke="#fff" stroke-width="1.3"/><circle cx="6" cy="9.4" r="0.7" fill="#fff"/></svg>
          <span>0438 175 906</span>
        </div>
        <div class="contact-line">
          <svg viewBox="0 0 12 12"><circle cx="6" cy="6" r="5" fill="none" stroke="#fff" stroke-width="1.3"/><path d="M1 6 H11 M6 1 C3.5 3.5 3.5 8.5 6 11 M6 1 C8.5 3.5 8.5 8.5 6 11" fill="none" stroke="#fff" stroke-width="1"/></svg>
          <span>gewservice.com.au</span>
        </div>
      </div>
    </div>

    <div class="brand-name">Gumtree<br>Engine Works</div>
  </section>

  <section class="card card--back">
    <div class="brand-name">Gumtree<br>Engine Works</div>
    <div class="emails">
      sales@gewservice.com.au | admin@gewservice.com.au | office@gewservice.com.au<br>
      reception@gewservice.com.au | accounts@gewservice.com.au | parts@gewservice.com.au
    </div>
  </section>
</body>
</html>
```